Brindlecove Partners needs a business card design

We need a new business card design using the logo recently selected in a logo competition on Pixel Arena. Our business is a consultancy specializing in aviation and energy and the winning business card design will promote an image of precision and professionalism with creativity.

Please use the logo with the name on the front of the card and use a complementary font. Make the back white with either the light grey or dark grey logo.

Target Market(s)

Senior finance and legal leaders at aviation and energy companies

Industry/Entity Type

Management Consulting

Contact Information for Business Card

Peter Dunstable
President
Brindlecove Partners

www.brindlecovepartners.example

(713) 555-0147
pd@brindlecovepartners.example

Requirements
Must have
• Professional font that goes well with the logo font

```html
<!DOCTYPE html>
<html lang="en">
<head>
<meta charset="UTF-8">
<title>Brindlecove Partners – Business Card</title>
<link href="https://fonts.googleapis.com/css2?family=Lato:wght@400;700&display=swap" rel="stylesheet">
<style>
  :root {
    --stage: #2b2b2d;
    --card: #ffffff;
    --navy: #17406f;
    --grey-mark: #8e8f93;
    --text-grey: #6a6b6e;
    --rule: #c9cacc;
  }
  * { margin: 0; padding: 0; box-sizing: border-box; }
  html, body {
    width: 1200px; height: 800px; overflow: hidden;
    background: var(--stage);
    font-family: "Lato", Arial, sans-serif;
  }
  .stage {
    width: 1200px; height: 800px;
    display: flex; align-items: center; justify-content: center; gap: 60px;
  }
  .card {
    position: relative;
    width: 520px; height: 298px;
    background: var(--card);
    box-shadow: 0 10px 28px rgba(0,0,0,.45);
    overflow: hidden;
  }
  /* Back */
  .card-back {
    display: flex; flex-direction: column; align-items: center; justify-content: center;
  }
  .back-name {
    color: var(--grey-mark);
    font-weight: 700;
    font-size: 40px;
    letter-spacing: 1px;
    margin-top: 10px;
  }
  .back-url {
    position: absolute; bottom: 34px; left: 0; right: 0;
    text-align: center;
    color: var(--text-grey);
    font-size: 14px;
    letter-spacing: .3px;
  }
  /* Front */
  .card-front { display: flex; }
  .front-brand {
    width: 270px;
    display: flex; align-items: center; justify-content: center; gap: 10px;
    padding-bottom: 28px;
  }
  .brand-square { width: 14px; height: 14px; background: var(--navy); flex: none; }
  .brand-name {
    color: var(--navy);
    font-size: 23px; font-weight: 400;
    letter-spacing: 1px;
  }
  .divider {
    position: absolute; left: 270px; top: 36px;
    width: 1px; height: 150px;
    background: var(--rule);
  }
  .front-contact {
    padding: 38px 0 0 18px;
  }
  .person-name { color: var(--navy); font-weight: 700; font-size: 17px; }
  .person-title { color: var(--text-grey); font-size: 12.5px; margin-top: 2px; }
  .contact-list { list-style: none; margin-top: 30px; }
  .contact-list li {
    display: flex; align-items: center; gap: 7px;
    color: var(--text-grey); font-size: 13px; line-height: 21px;
  }
  .contact-list svg { width: 12px; height: 12px; flex: none; fill: var(--navy); }
  .band {
    position: absolute; left: 0; right: 0; bottom: 0; height: 26px;
    background: var(--navy);
    border-top: 3px solid #9a9b9e;
  }
</style>
</head>
<body>
<main class="stage">
  <section class="card card-back" aria-label="Card back">
    <div class="back-name">Brindlecove Partners</div>
    <div class="back-url">www.brindlecovepartners.example</div>
  </section>

  <section class="card card-front" aria-label="Card front">
    <div class="front-brand">
      <span class="brand-square"></span>
      <span class="brand-name">Brindlecove Partners</span>
    </div>
    <div class="divider"></div>
    <div class="front-contact">
      <div class="person-name">Peter Dunstable</div>
      <div class="person-title">President</div>
      <ul class="contact-list">
        <li>
          <svg viewBox="0 0 24 24" aria-hidden="true"><path d="M6.6 10.8a15.1 15.1 0 0 0 6.6 6.6l2.2-2.2a1 1 0 0 1 1-.25 11.4 11.4 0 0 0 3.6.57 1 1 0 0 1 1 1V20a1 1 0 0 1-1 1A17 17 0 0 1 3 4a1 1 0 0 1 1-1h3.5a1 1 0 0 1 1 1 11.4 11.4 0 0 0 .57 3.6 1 1 0 0 1-.25 1z"/></svg>
          (713) 555-0147
        </li>
        <li>
          <svg viewBox="0 0 24 24" aria-hidden="true"><path d="M2 4h20v16H2zm2 2v.5l8 5 8-5V6zm0 2.8V18h16V8.8l-8 5z"/></svg>
          pd@brindlecovepartners.example
        </li>
        <li>
          <svg viewBox="0 0 24 24" aria-hidden="true"><path d="M12 2a10 10 0 1 0 0 20 10 10 0 0 0 0-20zm6.9 6h-3a15.6 15.6 0 0 0-1.3-3.9A8 8 0 0 1 18.9 8zM12 4c.8 1.2 1.5 2.5 1.9 4h-3.8c.4-1.5 1.1-2.8 1.9-4zM4.3 14a8 8 0 0 1 0-4h3.4a16 16 0 0 0 0 4zm.8 2h3a15.6 15.6 0 0 0 1.3 3.9A8 8 0 0 1 5.1 16zm3-8h-3a8 8 0 0 1 4.3-3.9A15.6 15.6 0 0 0 8.1 8zM12 20c-.8-1.2-1.5-2.5-1.9-4h3.8c-.4 1.5-1.1 2.8-1.9 4zm2.3-6H9.7a14 14 0 0 1 0-4h4.6a14 14 0 0 1 0 4zm.3 5.9a15.6 15.6 0 0 0 1.3-3.9h3a8 8 0 0 1-4.3 3.9zM16.3 14a16 16 0 0 0 0-4h3.4a8 8 0 0 1 0 4z"/></svg>
          www.brindlecovepartners.example
        </li>
      </ul>
    </div>
    <div class="band"></div>
  </section>
</main>
</body>
</html>
```